Packaging design for children’s shampoo bar

A design that could be used on solid shampoo and soap wraps then amended for jar labels. The packaging needs to be bright and child-friendly. We have a logo and a pattern, but please feel free to change them. I think it needs to be brighter.

I would like each product to have an accent colour and for the shampoo I am thinking of blue/teal. This will be complemented by the body wash bar (pink) and toothpaste (orange).

The shampoo bar wrap needs to contain the following information:

Pippin & Pals logo
Shampoo Bar
100% natural
Vegan & Palm Oil-Free
Weight 85 g
Made in the U.K.

Ingredients: sodium hydroxide, prunus amygdalus dulcis oil, olea europaea oil, cocos nucifera oil, ricinus communis seed oil, simmondsia chinensia seed oil.

Contact details: Pippin & Pals, Marlow Tessing House, London N7 4QB. Website: www.Pippin and pals.co.U.K.

Brand board is here: https://www.filecrate.example/s/k8rw2mzatqvexbd/Photo%2003-07-2020%2C%2021%2040%2034.jpg?dl=0

Inspiration is here: https://kitebirdstudio.example/collections/beauty-grooming/products/dog-shampoo-100-natural-vegan

These are the wraps we shall be using: https://www.nearbypressworks.example/soap-wrap

Thank you so much for your interest in this project!

Target Market(s)

Children 5-12 years.

Requirements
Must have
• Clean design. Lots of white with bright colours.

```html
<!DOCTYPE html>
<html lang="en">
<head>
<meta charset="utf-8">
<title>Pippin &amp; Pals Shampoo Bar Wrap</title>
<link rel="stylesheet" href="https://fonts.googleapis.com/css2?family=Montserrat:wght@300;400;500&family=Lobster&display=swap">
<style>
  :root{
    --page:#f4f4f2;
    --paper:#f3f2ef;
    --ink:#3d3d3d;
    --leaf:#8fb77e;
    --leaf-soft:#cfe0c4;
    --teal:#5f9fae;
    --pink:#c9659b;
    --coral:#e07a6c;
    --sand:#ecd6c0;
    --peach:#f1c79a;
    --script-green:#7aa840;
    --elephant:#d9854f;
    --dot:#2f2f2f;
  }
  *{box-sizing:border-box;margin:0;padding:0}
  html,body{width:1200px;height:1200px;overflow:hidden;background:var(--page)}
  body{position:relative;font-family:"Montserrat",sans-serif;color:var(--ink)}
  .wrap{position:absolute;left:240px;width:720px;height:530px;background:var(--paper);
        box-shadow:0 6px 18px rgba(0,0,0,.08);overflow:hidden}
  .wrap--front{top:40px}
  .wrap--back{top:630px}
  .wrap-art{position:absolute;inset:0;width:100%;height:100%}
  .brand{position:absolute;left:430px;transform:translateX(-50%);text-align:center;white-space:nowrap;
         font-weight:400;font-size:40px;letter-spacing:1px;color:var(--teal)}
  .brand::after{content:"";display:inline-block;width:10px;height:10px;border-radius:50%;
         background:var(--teal);margin-left:8px;vertical-align:middle}
  .wrap--front .brand{top:92px}
  .wrap--back .brand{top:52px}
  .product-title{position:absolute;left:430px;top:196px;transform:translateX(-50%) rotate(-4deg);
         font-family:"Lobster",cursive;font-size:50px;color:var(--script-green);white-space:nowrap}
  .mascot{position:absolute;left:375px;top:268px;width:140px;height:112px}
  .badges{position:absolute;left:430px;top:408px;transform:translateX(-50%);display:flex;gap:22px}
  .badge{width:52px;height:52px;border-radius:50%;border:3px solid var(--script-green);background:transparent}
  .facts{position:absolute;top:490px;left:300px;width:260px;display:flex;justify-content:space-between;
         font-size:15px;font-weight:300}
  .ingredients{position:absolute;left:430px;top:170px;transform:translateX(-50%);width:310px;text-align:center;
         font-size:15px;font-weight:300;line-height:1.45}
  .ingredients h2{font-size:15px;font-weight:500;margin-bottom:4px}
  .contact{position:absolute;left:430px;top:300px;transform:translateX(-50%);width:330px;text-align:center;
         font-size:15px;font-weight:300;line-height:1.5}
  .contact .company{font-size:20px;font-weight:500;line-height:1.4}
  .contact b{font-weight:500}
</style>
</head>
<body>

<section class="wrap wrap--front">
  <svg class="wrap-art" viewBox="0 0 720 530" aria-hidden="false">
    <rect x="0" y="0" width="150" height="530" fill="var(--leaf-soft)" opacity=".35"/>
    <g role="img" aria-label="Botanical illustration of leaves and pink flowers, top left">
      <ellipse cx="210" cy="50" rx="120" ry="90" fill="var(--leaf-soft)" opacity=".8"/>
      <ellipse cx="170" cy="40" rx="50" ry="40" fill="var(--pink)" opacity=".55"/>
    </g>
    <g role="img" aria-label="Beige blob with coral fern sprig, left">
      <ellipse cx="120" cy="200" rx="110" ry="60" fill="var(--sand)" opacity=".8"/>
      <ellipse cx="165" cy="230" rx="30" ry="45" fill="var(--coral)" opacity=".55"/>
    </g>
    <g role="img" aria-label="Green leaves, dotted pattern and yellow flower, bottom left">
      <ellipse cx="150" cy="430" rx="110" ry="90" fill="var(--leaf)" opacity=".5"/>
      <ellipse cx="210" cy="470" rx="45" ry="35" fill="var(--peach)" opacity=".8"/>
    </g>
    <g role="img" aria-label="Leaves, peach blob and flowers, top right">
      <ellipse cx="650" cy="120" rx="110" ry="100" fill="var(--leaf-soft)" opacity=".8"/>
      <ellipse cx="640" cy="170" rx="60" ry="50" fill="var(--peach)" opacity=".7"/>
    </g>
    <g role="img" aria-label="Green leaf and magenta flower, bottom right">
      <ellipse cx="680" cy="360" rx="50" ry="80" fill="var(--leaf)" opacity=".55"/>
      <ellipse cx="650" cy="470" rx="70" ry="55" fill="var(--pink)" opacity=".6"/>
    </g>
  </svg>
  <div class="brand">Pippin &amp; Pals</div>
  <div class="product-title">Shampoo Bar</div>
  <svg class="mascot" viewBox="0 0 140 112" role="img" aria-label="Illustration of an orange baby elephant spraying water">
    <ellipse cx="78" cy="60" rx="58" ry="46" fill="var(--elephant)"/>
  </svg>
  <div class="badges">
    <span class="badge" title="100% natural"></span>
    <span class="badge" title="Palm oil free"></span>
    <span class="badge" title="Certified vegan"></span>
  </div>
  <div class="facts"><span>Weight 85 g</span><span>Made in U.K.</span></div>
</section>

<section class="wrap wrap--back">
  <svg class="wrap-art" viewBox="0 0 720 530">
    <rect x="0" y="0" width="150" height="530" fill="var(--leaf-soft)" opacity=".35"/>
    <g role="img" aria-label="Botanical illustration of leaves and pink flowers, top left">
      <ellipse cx="210" cy="50" rx="120" ry="90" fill="var(--leaf-soft)" opacity=".8"/>
      <ellipse cx="170" cy="40" rx="50" ry="40" fill="var(--pink)" opacity=".45"/>
    </g>
    <g role="img" aria-label="Beige blob with coral fern sprig, left">
      <ellipse cx="120" cy="200" rx="110" ry="60" fill="var(--sand)" opacity=".7"/>
      <ellipse cx="165" cy="240" rx="30" ry="45" fill="var(--coral)" opacity=".45"/>
    </g>
    <g role="img" aria-label="Green leaves, dotted pattern and yellow flower, bottom left">
      <ellipse cx="150" cy="430" rx="110" ry="90" fill="var(--leaf)" opacity=".45"/>
      <ellipse cx="210" cy="470" rx="45" ry="35" fill="var(--peach)" opacity=".7"/>
    </g>
    <g role="img" aria-label="Leaves, peach blob and flowers, top right">
      <ellipse cx="650" cy="120" rx="110" ry="100" fill="var(--leaf-soft)" opacity=".7"/>
      <ellipse cx="640" cy="170" rx="60" ry="50" fill="var(--peach)" opacity=".6"/>
    </g>
    <g role="img" aria-label="Green leaf and magenta flower, bottom right">
      <ellipse cx="680" cy="360" rx="50" ry="80" fill="var(--leaf)" opacity=".5"/>
      <ellipse cx="650" cy="470" rx="70" ry="55" fill="var(--pink)" opacity=".5"/>
    </g>
  </svg>
  <div class="brand">Pippin &amp; Pals</div>
  <div class="ingredients">
    <h2>INGREDIENTS:</h2>
    <p>Sodium Hydroxide, Prunus Amygdalus Dulcis Oil, Olea Europaea Oil, Cocos Nucifera Oil, Ricinus Communis Seed Oil, Simmondsia Chinensia Seed Oil.</p>
  </div>
  <div class="contact">
    <p>Contact Details:</p>
    <p class="company">Pippin &amp; Pals,</p>
    <p>Marlow Tessing House, London N7 4QB.</p>
    <p><b>Website:</b> www.Pippin and pals.co.U.K.</p>
  </div>
</section>

</body>
</html>
```